Mechanical Engineer Business Card Design (Unemployed)

I am unemployed and actively looking for a job in Canada. I will be using this business card when I meet potential employers or in networking events.I would love to have the engraved writing style (as if it is engraved on the card). Some examples attached.I would love to have a personalized logo that represents my 2 majors. The final design should have a professional look that can stand out if attached to a resume. Jobs I am applying for are in construction, mining, oil and gas, Aerospace, manufacturing and whatever field I can be integrated in.A metallic look on the back is ok. but the front have to be sort of can be written on. you can also try to add my linkedin profile https://ca.folionet.example/in/doruvelsh
On the front or back, I would love to have the symbol of mail and phone rather than the words. that saves spaceAmaze me guys.

Target Market(s)

Engineering

Industry/Entity Type

Engineering

Contact Information for Business Card

Doru Velsh
Mechanical Engineer

Phone number: +1 (555) 014 - 2736
email: velshdoru@mailbrook.example

Font styles to use
Serif
Sans Serif
Decorative
Script

Requirements
Must have
• PERSONALIZED and brand new Simple Logo
• Professional look
• Engraved writing for the name
• Help stand out when attached on CV
Nice to have
• Metallic back look

```html
<!DOCTYPE html>
<html lang="en">
<head>
<meta charset="utf-8">
<title>Doru Velsh — Business Card</title>
<link rel="stylesheet" href="https://fonts.googleapis.com/css2?family=Tinos:wght@400;700&display=swap">
<style>
  :root {
    --page-bg: #e7e5e2;
    --card-white: #ffffff;
    --card-shade: #ebebeb;
    --ink: #1b1b1b;
    --ink-soft: #2e2e2e;
    --band-black: #050505;
    --band-red: #e2383f;
    --engrave-light: rgba(255,255,255,0.9);
    --engrave-dark: rgba(0,0,0,0.35);
  }
  * { box-sizing: border-box; margin: 0; padding: 0; }
  html, body { width: 1200px; height: 892px; overflow: hidden; }
  body {
    background: var(--page-bg);
    font-family: "Tinos", "Times New Roman", serif;
    color: var(--ink);
    position: relative;
  }
  .card {
    position: absolute;
    left: 320px;
    width: 560px;
    height: 320px;
    background: radial-gradient(ellipse at 45% 40%, var(--card-white) 0%, var(--card-shade) 100%);
    box-shadow: 0 6px 18px rgba(0,0,0,0.18);
    overflow: hidden;
  }
  .card--front { top: 100px; }
  .card--back { top: 472px; }

  .card__band { position: absolute; inset: 0; width: 560px; height: 320px; }

  .identity { position: absolute; left: 40px; top: 52px; }
  .identity__name {
    font-size: 38px;
    font-weight: 400;
    letter-spacing: 0.5px;
    color: var(--ink);
    text-shadow: 0 1px 0 var(--engrave-light), 0 -1px 0 var(--engrave-dark);
    line-height: 1;
  }
  .identity__role { font-size: 18px; margin-top: 8px; line-height: 1.05; }
  .identity__degree { font-size: 16px; line-height: 1.2; color: var(--ink-soft); }
  .identity__degree--first { margin-top: 4px; margin-left: 14px; }
  .identity__degree--second { margin-left: 28px; }

  .contact { position: absolute; left: 40px; top: 196px; list-style: none; }
  .contact__item {
    display: flex; align-items: center; gap: 12px;
    font-size: 16px; color: var(--ink-soft); height: 24px;
  }
  .contact__icon { width: 14px; height: 14px; flex: none; }

  .mark {
    position: absolute;
    display: flex; align-items: center; gap: 10px;
    font-size: 22px; font-weight: 700; color: var(--ink);
  }
  .card--front .mark { left: 330px; top: 44px; }
  .card--back .mark { left: 50%; top: 50%; transform: translate(-50%, -50%); font-size: 30px; }
  .mark__dot { width: 20px; height: 20px; border-radius: 50%; background: var(--ink); }
  .card--back .mark__dot { width: 26px; height: 26px; }
</style>
</head>
<body>
  <section class="card card--front" aria-label="Business card front">
    <svg class="card__band" viewBox="0 0 560 320" aria-hidden="true">
      <path d="M0 262 C120 262 230 262 300 230 C360 190 380 120 440 100 C490 84 530 86 560 86 L560 320 L0 320 Z" fill="var(--band-red)"/>
      <path d="M0 278 C130 278 250 276 320 240 C380 200 400 130 450 108 C495 90 530 90 560 90 L560 320 L0 320 Z" fill="var(--band-black)"/>
    </svg>

    <div class="mark">
      <span class="mark__dot"></span>
      <span class="mark__name">Velsh Mechanics</span>
    </div>

    <div class="identity">
      <h1 class="identity__name">Doru Velsh</h1>
      <p class="identity__role">Field Mechanical Engineer</p>
      <p class="identity__degree identity__degree--first">Mechanical Engineer (B.Sc.)</p>
      <p class="identity__degree identity__degree--second">Aerospace Engineer (M.Sc.)</p>
    </div>

    <ul class="contact">
      <li class="contact__item">
        <svg class="contact__icon" viewBox="0 0 14 14" aria-label="Phone">
          <rect width="14" height="14" fill="var(--ink)"/>
          <path d="M4 3 L5.5 3 L6 5 L5 6 C5.5 7.2 6.8 8.5 8 9 L9 8 L11 8.5 L11 10 C11 10.6 10.5 11 10 11 C6.5 11 3 7.5 3 4 C3 3.5 3.4 3 4 3 Z" fill="#fff"/>
        </svg>
        <span>(+1) 555 - 014 - 2736</span>
      </li>
      <li class="contact__item">
        <svg class="contact__icon" viewBox="0 0 14 14" aria-label="Email">
          <rect width="14" height="14" fill="var(--ink)"/>
          <rect x="3" y="4" width="8" height="6" fill="#fff"/>
          <path d="M3 4 L7 7.5 L11 4" fill="none" stroke="var(--ink)" stroke-width="1"/>
        </svg>
        <span>velshdoru@mailbrook.example</span>
      </li>
    </ul>
  </section>

  <section class="card card--back" aria-label="Business card back">
    <div class="mark">
      <span class="mark__dot"></span>
      <span class="mark__name">Velsh Mechanics</span>
    </div>
  </section>
</body>
</html>
```